"Wellenhafen" private practice for physiotherapy

we are looking for a flyer design for a private practice for physiotherapy. the name of the practice is "Wellenhafen".
Treatments such as: manual therapy, manual lymphatic drainage, classic massage, sectoral alternative practitioners are offered

The flyers should be double-sided and the format DIN long (105x210 mm)

Font styles to use
Serif

Colors
0094D4
00A9DD
6FCCEA
C7EBF8
E9F6FB

Requirements
Must have
• Wellenhafen, Lindenweg 17, 04719 Sangerhausen / Wellenhafen-praxis-beispiel.de / Tel. 03471 5820317

```html
<!DOCTYPE html>
<html lang="de">
<head>
<meta charset="utf-8">
<title>Wellenhafen – Flyer DIN lang</title>
<link rel="stylesheet" href="https://fonts.googleapis.com/css2?family=Open+Sans:wght@400;600;700;800&display=swap">
<style>
  :root{
    --stage:#03141c;
    --blue-deep:#12338f;
    --blue-mid:#1d5fb5;
    --blue-bright:#0094d4;
    --blue-sky:#00a9dd;
    --blue-light:#6fccea;
    --blue-pale:#c7ebf8;
    --blue-mist:#e9f6fb;
    --navy-text:#141f7a;
    --white:#ffffff;
    --paper:#f2f3f5;
    --map-grey:#d9dcdf;
  }
  *{box-sizing:border-box;margin:0;padding:0}
  html,body{width:1200px;height:1200px;overflow:hidden;background:var(--stage)}
  body{font-family:"Open Sans",Arial,sans-serif;position:relative}
  .flyer{position:absolute;top:180px;width:420px;height:840px;overflow:hidden;background:var(--paper)}
  .flyer--back{left:150px}
  .flyer--front{left:630px;background:var(--white)}
  .flyer__art{position:absolute;inset:0}

  /* back side */
  .back__title{position:absolute;top:60px;width:100%;text-align:center;color:var(--white);font-weight:700;font-size:34px;line-height:1.3;letter-spacing:-.3px}
  .service-grid{position:absolute;top:130px;left:40px;right:40px;display:grid;grid-template-columns:1fr 1fr;row-gap:26px;column-gap:10px}
  .service{display:flex;flex-direction:column;align-items:center;text-align:center;color:var(--white);font-size:22px;line-height:1.3;font-weight:400}
  .service svg{width:42px;height:42px;margin-bottom:8px}
  .map-box{position:absolute;left:135px;top:470px;width:260px;height:185px;background:var(--map-grey);border:5px solid #9ea3a8}
  .back__address{position:absolute;top:678px;left:0;right:0;text-align:center;color:#111;font-size:23px;line-height:1.35}
  .back__web{position:absolute;top:748px;left:0;right:0;text-align:center;color:var(--navy-text);font-size:14px;line-height:1.4;font-weight:600}
  .back__phone{position:absolute;top:770px;left:0;right:0;text-align:center;color:var(--navy-text);font-size:30px;line-height:1.2;font-weight:800}

  /* front side */
  .front__title{position:absolute;top:470px;left:40px;color:var(--white);font-weight:700;font-size:36px;line-height:1.3;letter-spacing:-.3px}
  .treatments{position:absolute;top:528px;left:40px;list-style:none;color:var(--white);font-size:22px;line-height:1.3}
  .treatments li{display:flex;align-items:flex-start;gap:8px;margin-bottom:2px}
  .treatments svg{flex:0 0 22px;width:22px;height:22px;margin-top:4px}
  .front__web{position:absolute;top:738px;left:40px;color:var(--navy-text);font-size:17px;line-height:1.4;font-weight:600}
  .front__phone{position:absolute;top:762px;left:40px;color:var(--navy-text);font-size:40px;line-height:1.2;font-weight:800;letter-spacing:-.3px}
</style>
</head>
<body>

<section class="flyer flyer--back" aria-label="Flyer Rückseite">
  <svg class="flyer__art" viewBox="0 0 420 840" aria-hidden="true">
    <defs>
      <linearGradient id="backBlue" x1="0" y1="0" x2="0" y2="1">
        <stop offset="0" stop-color="#1a7fd6"/>
        <stop offset=".6" stop-color="#1e63c4"/>
        <stop offset="1" stop-color="#1c4fb0"/>
      </linearGradient>
    </defs>
    <path d="M0 0H420V500C330 520 180 555 0 560Z" fill="url(#backBlue)"/>
    <path d="M0 560C180 555 330 520 420 500V512C330 532 180 568 0 572Z" fill="var(--blue-deep)"/>
  </svg>
  <div role="img" aria-label="Foto einer Patientin bei der Schulterbehandlung, blau eingefärbt" style="position:absolute;left:0;top:0;width:420px;height:500px;background:radial-gradient(ellipse at 45% 30%,rgba(111,204,234,.35),rgba(0,148,212,0) 60%)"></div>
  <h2 class="back__title">Wellenhafen</h2>
  <div class="service-grid">
    <div class="service"><svg viewBox="0 0 42 42"><circle cx="21" cy="21" r="17" fill="none" stroke="#fff" stroke-width="3"/><path d="M12 21l7 8 15-20" fill="none" stroke="#fff" stroke-width="4" stroke-linecap="round" stroke-linejoin="round"/></svg>Manual<br>Therapy</div>
    <div class="service"><svg viewBox="0 0 42 42"><circle cx="21" cy="21" r="17" fill="none" stroke="#fff" stroke-width="3"/><path d="M12 21l7 8 15-20" fill="none" stroke="#fff" stroke-width="4" stroke-linecap="round" stroke-linejoin="round"/></svg>Classic<br>Massage</div>
    <div class="service"><svg viewBox="0 0 42 42"><circle cx="21" cy="21" r="17" fill="none" stroke="#fff" stroke-width="3"/><path d="M12 21l7 8 15-20" fill="none" stroke="#fff" stroke-width="4" stroke-linecap="round" stroke-linejoin="round"/></svg>Sectoral<br>Alternative<br>Practitioners</div>
    <div class="service"><svg viewBox="0 0 42 42"><circle cx="21" cy="21" r="17" fill="none" stroke="#fff" stroke-width="3"/><path d="M12 21l7 8 15-20" fill="none" stroke="#fff" stroke-width="4" stroke-linecap="round" stroke-linejoin="round"/></svg>Manual<br>Lymphatic<br>Drainage</div>
  </div>
  <div class="map-box" role="img" aria-label="Stadtplanausschnitt mit Lage der Praxis"></div>
  <p class="back__address">Lindenweg 17<br>04719 Sangerhausen</p>
  <p class="back__web">Wellenhafen-praxis-beispiel.de</p>
  <p class="back__phone">03471 5820317</p>
</section>

<section class="flyer flyer--front" aria-label="Flyer Vorderseite">
  <svg class="flyer__art" viewBox="0 0 420 840" aria-hidden="true">
    <defs>
      <linearGradient id="frontBlue" x1="0" y1="0" x2="1" y2="1">
        <stop offset="0" stop-color="#1f6fc8"/>
        <stop offset=".55" stop-color="#1d52ac"/>
        <stop offset="1" stop-color="#182f8a"/>
      </linearGradient>
    </defs>
    <path d="M230 0C330 20 400 70 420 110V720C300 735 140 712 0 700V380C120 360 200 300 230 0Z" fill="url(#frontBlue)"/>
    <path d="M0 700C140 712 300 735 420 720V732C300 748 140 724 0 712Z" fill="var(--blue-deep)"/>
    <circle cx="355" cy="250" r="152" fill="#1b3f96"/>
    <circle cx="250" cy="380" r="100" fill="#2a3a6a"/>
  </svg>
  <div role="img" aria-label="Foto eines Therapeuten bei der Rückenbehandlung" style="position:absolute;left:0;top:0;width:300px;height:380px;border-bottom-right-radius:160px 210px;background:linear-gradient(160deg,#f4f6f8,#c9d3dc 55%,#6f9ac7)"></div>
  <div role="img" aria-label="Foto einer Beinbehandlung auf der Liege" style="position:absolute;left:212px;top:106px;width:288px;height:288px;border-radius:50%;background:linear-gradient(150deg,#e8eef1,#c7d2d8 60%,#a8b6bf)"></div>
  <div role="img" aria-label="Foto einer Kniebehandlung" style="position:absolute;left:158px;top:284px;width:184px;height:184px;border-radius:50%;background:linear-gradient(140deg,#cfd6dc,#7c8791 60%,#4a525b)"></div>
  <h1 class="front__title">Wellenhafen</h1>
  <ul class="treatments">
    <li><svg viewBox="0 0 22 22"><circle cx="11" cy="11" r="9" fill="none" stroke="#fff" stroke-width="2"/><path d="M6 11l4 4 8-10" fill="none" stroke="#fff" stroke-width="2.5" stroke-linecap="round" stroke-linejoin="round"/></svg>Manual Therapy</li>
    <li><svg viewBox="0 0 22 22"><circle cx="11" cy="11" r="9" fill="none" stroke="#fff" stroke-width="2"/><path d="M6 11l4 4 8-10" fill="none" stroke="#fff" stroke-width="2.5" stroke-linecap="round" stroke-linejoin="round"/></svg><span>Manual Lymphatic<br>Drainage</span></li>
    <li><svg viewBox="0 0 22 22"><circle cx="11" cy="11" r="9" fill="none" stroke="#fff" stroke-width="2"/><path d="M6 11l4 4 8-10" fill="none" stroke="#fff" stroke-width="2.5" stroke-linecap="round" stroke-linejoin="round"/></svg>Classic Massage</li>
    <li><svg viewBox="0 0 22 22"><circle cx="11" cy="11" r="9" fill="none" stroke="#fff" stroke-width="2"/><path d="M6 11l4 4 8-10" fill="none" stroke="#fff" stroke-width="2.5" stroke-linecap="round" stroke-linejoin="round"/></svg><span>Sectoral Alternative<br>Practitioners</span></li>
  </ul>
  <p class="front__web">Wellenhafen-praxis-beispiel.de</p>
  <p class="front__phone">03471 5820317</p>
</section>

</body>
</html>
```